Company Flyer for Electric boating company

I am looking for a company flyer which we can hand over to boat owners in the Netherlands (Amsterdam area). Our core business is to rebuild every boat (from 4 to 10 meters) into an electrically propelled boat. We are taking out diesels and replace them with a high quality electrical motor, inboard varying from 30 till 80 pk (hp). And outboard from 1pk (hp) till 200pk. We are the best, not the cheapest, not the most expensive. We only work with the best materials. The flyer has to be sort of in line with our website and branding.

Major advantages of electric boating are:
- completely silent
- no fumes, smells or smoke
- cheap to operate
- environmentally friendly
- obliged in more and more areas
- no maintenance
- more enjoyable

The flyer should be A5 format. Since all the text has to be in Dutch I expect only the graphical design and layout for advantages, process, pricing and contact details etc.

Target Market(s)

Boat owners in the Netherlands

Font styles to use
Sans Serif

Colors
9bcb3c
add136
cadf82
0555a3
3176b5
85acd3
e0ebf3

Requirements
Must have
• Clean design, in line with website: www.volta-kade.nl
Nice to have
• icons for advantages, boating etc

2 sides
Should not have
• Steering wheel...

```html
<!DOCTYPE html>
<html lang="en">
<head>
<meta charset="utf-8">
<title>Volta-Kade flyer</title>
<link href="https://fonts.googleapis.com/css2?family=Open+Sans:wght@400;600&display=swap" rel="stylesheet">
<style>
  :root {
    --green: #9bcb3c;
    --green-bright: #add136;
    --blue-dark: #0555a3;
    --blue-mid: #3176b5;
    --blue-light: #85acd3;
    --blue-pale: #e0ebf3;
    --white: #ffffff;
    --sea-top: #3bb0d6;
    --sea-mid: #1a7fa6;
    --sea-deep: #0f5b73;
    --seabed: #3f6b3a;
  }
  html, body {
    margin: 0;
    padding: 0;
    overflow: hidden;
    background: #ffffff;
  }
  .flyer {
    position: relative;
    width: 847px;
    height: 1200px;
    overflow: hidden;
    font-family: "Open Sans", Arial, sans-serif;
    color: var(--white);
  }
  .underwater-photo {
    position: absolute;
    inset: 0;
    background:
      radial-gradient(ellipse 180px 420px at 430px 260px, rgba(10,50,70,0.75), rgba(10,50,70,0) 100%),
      linear-gradient(180deg, var(--sea-top) 0%, var(--sea-mid) 35%, var(--sea-deep) 62%, #1d6a6e 80%, var(--seabed) 100%);
  }
  .headline {
    position: absolute;
    left: 113px;
    top: 580px;
    margin: 0;
    font-weight: 400;
    font-size: 46px;
    line-height: 78px;
    letter-spacing: 0.3px;
    white-space: nowrap;
  }
  .brand-band {
    position: absolute;
    left: 0;
    top: 758px;
    width: 847px;
    height: 104px;
    display: flex;
  }
  .brand-band .stripe { height: 100%; }
  .stripe-dark { width: 30px; background: var(--blue-dark); }
  .stripe-mid { width: 26px; background: var(--blue-mid); }
  .stripe-light { width: 22px; background: var(--blue-light); }
  .stripe-pale { width: 20px; background: var(--blue-pale); }
  .brand-panel {
    flex: 1;
    background: var(--white);
    display: flex;
    align-items: center;
    padding-left: 244px;
    gap: 20px;
  }
  .brand-dot {
    width: 84px;
    height: 84px;
    border-radius: 50%;
    background: var(--green);
  }
  .brand-name {
    font-weight: 600;
    font-size: 48px;
    color: var(--green);
    letter-spacing: 1px;
    white-space: nowrap;
  }
  .advantages {
    position: absolute;
    left: 428px;
    top: 900px;
    margin: 0;
    padding: 0;
    list-style: none;
    font-size: 24px;
    line-height: 40px;
    white-space: nowrap;
  }
  .advantages li::before { content: "- "; }
</style>
</head>
<body>
  <main class="flyer">
    <div class="underwater-photo" role="img" aria-label="Underwater view of a boat hull seen from below, sunlit blue water with fish and a green seabed"></div>

    <h1 class="headline">Rebuild Into An<br>Electrically Propelled Boat</h1>

    <div class="brand-band">
      <div class="stripe stripe-dark"></div>
      <div class="stripe stripe-mid"></div>
      <div class="stripe stripe-light"></div>
      <div class="stripe stripe-pale"></div>
      <div class="brand-panel">
        <span class="brand-dot"></span>
        <span class="brand-name">VOLTA-KADE</span>
      </div>
    </div>

    <ul class="advantages">
      <li>completely silent</li>
      <li>no fumes, smells or smoke</li>
      <li>cheap to operate</li>
      <li>environmentally friendly</li>
      <li>obliged in more and more areas</li>
      <li>no maintenance</li>
      <li>more enjoyable</li>
    </ul>
  </main>
</body>
</html>
```